Compnay PowerPoint Tempalte Design

I am needing a good base design and slide designs for interior and exterior company presentations. The template will need to be on the company brand with proper coloring and fonts. Able to be creative with layout options with a good example attached.
website for reference: www.crewplorvane.com/

Target Market(s)

Professionals

Font styles to use
Other font styles liked:
• Helvetica

Requirements
Must have
• On Brand Colors, Clean, simple design

```html
<!DOCTYPE html>
<html lang="en">
<head>
<meta charset="utf-8">
<title>Plorvane Presentation Template</title>
<link href="https://fonts.googleapis.com/css2?family=Arimo:wght@400;700&display=swap" rel="stylesheet">
<style>
:root{
  --bg:#c9c9cb;
  --teal:#2f9e94;
  --teal-light:#8fd0c6;
  --teal-pale:#d3ece8;
  --blue:#1f7fa8;
  --navy:#1b5f80;
  --ink:#13232a;
  --grey:#6b7479;
  --white:#ffffff;
  --row:#eef4f4;
}
*{box-sizing:border-box;margin:0;padding:0}
html,body{width:1200px;height:3672px;overflow:hidden;background:var(--bg)}
body{font-family:"Arimo",Helvetica,Arial,sans-serif;color:var(--ink)}
.sheet{position:relative;width:1200px;height:3672px;overflow:hidden;background:var(--bg)}
.slide{position:absolute;width:540px;height:303px;background:var(--white);overflow:hidden}
.hero{left:225px;top:88px;transform:scale(1.3907);transform-origin:0 0}
.abs{position:absolute}
.c{text-align:center}
.photo{position:absolute}

/* cover */
.cover-top{position:absolute;left:46px;top:20px;font-size:6px;color:var(--grey);line-height:1.35}
.cover-top.url{color:#4f8e99;font-size:7px;top:21px}
.cover-photo{position:absolute;inset:0;clip-path:polygon(0 45px,395px 45px,440px 108px,540px 108px,540px 288px,0 288px)}
.cover--teal .cover-photo{background:linear-gradient(115deg,#3ea79c 0%,#2f958f 45%,#276f7f 75%,#2d6579 100%)}
.cover--dark .cover-photo{background:linear-gradient(115deg,#1e2b31 0%,#26404a 45%,#2d5e6a 75%,#3a7a84 100%)}
.cover-edge{position:absolute;left:0;top:0}
.brand{position:absolute;right:22px;top:54px;font-size:21px;font-weight:700;color:var(--ink);letter-spacing:.5px}
.brand::before{content:"";position:absolute;left:-12px;top:6px;width:8px;height:8px;background:var(--teal)}
.cover-text{position:absolute;left:46px;top:108px}
.cover-text h1{font-size:29px;font-weight:700;line-height:1;letter-spacing:.2px}
.cover-text h2{font-size:26px;font-weight:400;line-height:1.15;padding-bottom:4px;border-bottom:1.5px solid currentColor;display:inline-block;padding-right:4px}
.cover-text .sub{font-size:14px;margin-top:6px}
.cover-text .date{font-size:7px;margin-top:26px}
.cover--teal .cover-text{color:#0b1619}
.cover--dark .cover-text{color:var(--white)}
.cover-foot{position:absolute;left:0;right:0;bottom:0;height:15px;font-size:5px;color:#fff;text-align:center;line-height:15px;padding-left:70px}
.cover--teal .cover-foot{background:#226a6c}
.cover--dark .cover-foot{background:#1a2529}

/* interior shared */
.mark{position:absolute;left:0;right:0;text-align:center;font-size:7px;font-weight:700;color:var(--teal);letter-spacing:1px}
.title{position:absolute;left:0;right:0;text-align:center;font-size:19px;color:var(--ink)}
.title b{font-weight:700}
.foot-name{position:absolute;left:10px;bottom:5px;font-size:9px;font-weight:700;color:var(--ink)}
.foot-bar{position:absolute;left:62px;right:10px;bottom:8px;height:7px;background:linear-gradient(90deg,var(--teal),var(--blue));font-size:4px;color:#fff;text-align:right;line-height:7px;padding-right:8px}
.on-dark .foot-name{color:var(--white)}
.txt{font-size:6.5px;color:var(--grey);line-height:1.3}
.h-teal{color:var(--teal);font-size:10px}
.h-bold{font-weight:700;color:var(--teal);font-size:9.5px}

/* toc */
.toc-item{position:absolute;width:190px;display:flex;gap:12px}
.toc-num{font-size:18px;color:#b8bec1;width:16px}
.toc-item .txt{font-size:6px}

/* framed photo */
.frame{position:absolute;border:2px solid var(--teal)}
.frame-block{position:absolute;background:var(--teal)}

/* header band */
.band{position:absolute;left:0;top:0;width:540px;height:150px;background:linear-gradient(110deg,#3aa49a 0%,#2f8f96 50%,#2a7a93 100%)}
.band-title{position:absolute;left:0;right:0;top:46px;text-align:center;color:#fff;font-size:19px}
.band-title b{font-weight:700}
.band-text{position:absolute;left:60px;right:60px;top:88px;text-align:center;color:#e7f5f3;font-size:7.5px;line-height:1.3}
.col{position:absolute;width:110px;text-align:center}
.col .txt{margin-top:5px}

/* team */
.avatar{position:absolute;width:72px;height:72px;border-radius:50%;border:3px solid #fff;background:radial-gradient(circle at 50% 40%,#d8dcdc,#8b979b)}

/* icons */
.ico{position:absolute;width:20px;height:20px;border-radius:50%;display:flex;align-items:center;justify-content:center}
.ico svg{width:11px;height:11px}
.t{background:var(--teal)} .d{background:var(--ink)} .b{background:var(--blue)} .l{background:#7cc3b8}
.item{position:absolute;width:200px;padding-left:32px}
.item .h-teal{font-size:8.5px}
.item .txt{font-size:5.5px}

/* process */
.step{position:absolute;width:30px;height:30px;border-radius:50%;color:#fff;font-weight:700;font-size:14px;text-align:center;line-height:30px;border:3px solid #d7eeeb}

/* tables */
table{border-collapse:collapse;width:100%}
.mini td,.mini th{font-size:5.5px;padding:2.5px 4px;text-align:left}
.mini th{background:var(--ink);color:#fff}
.mini th.s{background:var(--teal);text-align:center}
.mini td.n{text-align:center}
.mini tr:nth-child(even) td{background:var(--row)}
.big td,.big th{font-size:6.5px;padding:4.2px 5px;text-align:center;border-bottom:1px solid #dde6e7}
.big th{background:var(--blue);color:#fff;font-weight:700}
.big th:first-child{background:var(--teal);text-align:left}
.big td:first-child{text-align:left;color:var(--grey)}
.big tr:nth-child(even) td{background:var(--row)}

/* contact */
.contact{background:linear-gradient(125deg,#22353b 0%,#23484f 50%,#2a6a6c 100%)}
.contact-list{position:absolute;left:55px;top:160px;color:#fff;font-size:7px}
.contact-list li{list-style:none;display:flex;align-items:center;gap:6px;margin-bottom:6px}
.contact-list svg{width:8px;height:8px}
</style>
</head>
<body>
<main class="sheet">

<!-- hero cover -->
<section class="slide cover cover--dark hero">
  <div class="cover-photo" role="img" aria-label="Team hands joined over a desk with laptops, dark teal tint"></div>
  <svg class="cover-edge" width="540" height="303"><polyline points="0,41 397,41 442,104 540,104" fill="none" stroke="#cfe9e6" stroke-width="4"/></svg>
  <p class="cover-top url">https://www.crewplorvane.com</p>
  <div class="brand">Plorvane</div>
  <div class="cover-text"><h1>PRESENTATION</h1><h2>Title Goes Here!</h2><p class="sub">Subtitle of Presentation Goes Here!</p><p class="date">September 27, 2021</p></div>
  <div class="cover-foot">Copyright 2021 Plorvane. All rights reserved</div>
</section>

<!-- row 1 -->
<section class="slide cover cover--teal" style="left:51px;top:740px">
  <div class="cover-photo" role="img" aria-label="Team hands joined over a desk, teal tint"></div>
  <svg class="cover-edge" width="540" height="303"><polyline points="0,41 397,41 442,104 540,104" fill="none" stroke="#cfe9e6" stroke-width="4"/></svg>
  <p class="cover-top url">https://www.crewplorvane.com</p>
  <div class="brand">Plorvane</div>
  <div class="cover-text"><h1>PRESENTATION</h1><h2>Title Goes Here!</h2><p class="sub">Subtitle of Presentation Goes Here!</p><p class="date">September 27, 2021</p></div>
  <div class="cover-foot">Copyright 2021 Plorvane. All rights reserved</div>
</section>
<section class="slide cover cover--dark" style="left:609px;top:740px">
  <div class="cover-photo" role="img" aria-label="Team hands joined over a desk, dark tint"></div>
  <svg class="cover-edge" width="540" height="303"><polyline points="0,41 397,41 442,104 540,104" fill="none" stroke="#cfe9e6" stroke-width="4"/></svg>
  <p class="cover-top url">https://www.crewplorvane.com</p>
  <div class="brand">Plorvane</div>
  <div class="cover-text"><h1>PRESENTATION</h1><h2>Title Goes Here!</h2><p class="sub">Subtitle of Presentation Goes Here!</p><p class="date">September 27, 2021</p></div>
  <div class="cover-foot">Copyright 2021 Plorvane. All rights reserved</div>
</section>

<!-- row 2 -->
<section class="slide cover cover--teal" style="left:51px;top:1060px">
  <div class="cover-photo" role="img" aria-label="Laptop and documents on a wooden desk, teal tint"></div>
  <svg class="cover-edge" width="540" height="303"><polyline points="0,41 397,41 442,104 540,104" fill="none" stroke="#cfe9e6" stroke-width="4"/></svg>
  <p class="cover-top">Where we maintain a passion for excellence, striving to be better each and every<br>day, so that our guests leave happy and our team members feel fulfilled.</p>
  <div class="brand">Plorvane</div>
  <div class="cover-text"><h1>PRESENTATION</h1><h2>Title Goes Here!</h2><p class="sub">Subtitle of Presentation Goes Here!</p><p class="date">September 27, 2021</p></div>
  <div class="cover-foot">Copyright 2021 Plorvane. All rights reserved</div>
</section>
<section class="slide cover cover--dark" style="left:609px;top:1060px">
  <div class="cover-photo" role="img" aria-label="Laptop and documents on a wooden desk, dark tint"></div>
  <svg class="cover-edge" width="540" height="303"><polyline points="0,41 397,41 442,104 540,104" fill="none" stroke="#cfe9e6" stroke-width="4"/></svg>
  <p class="cover-top">Where we maintain a passion for excellence, striving to be better each and every<br>day, so that our guests leave happy and our team members feel fulfilled.</p>
  <div class="brand">Plorvane</div>
  <div class="cover-text"><h1>PRESENTATION</h1><h2>Title Goes Here!</h2><p class="sub">Subtitle of Presentation Goes Here!</p><p class="date">September 27, 2021</p></div>
  <div class="cover-foot">Copyright 2021 Plorvane. All rights reserved</div>
</section>

<!-- row 3: contents, about -->
<section class="slide toc" style="left:51px;top:1382px">
  <p class="mark" style="top:20px">PLORVANE</p>
  <h2 class="title" style="top:42px;font-weight:400">Table of Contents</h2>
  <div class="toc-item" style="left:72px;top:103px"><span class="toc-num">1</span><div><p class="h-teal">Title Goes Here!</p><p class="txt">Lorem ipsum dolor sit amet, consectetur adipiscing elit. Vivamus eu dui ex.</p></div></div>
  <div class="toc-item" style="left:285px;top:103px"><span class="toc-num">2</span><div><p class="h-teal">Title Goes Here!</p><p class="txt">Lorem ipsum dolor sit amet, consectetur adipiscing elit. Vivamus eu dui ex.</p></div></div>
  <div class="toc-item" style="left:72px;top:156px"><span class="toc-num">3</span><div><p class="h-teal">Title Goes Here!</p><p class="txt">Lorem ipsum dolor sit amet, consectetur adipiscing elit. Vivamus eu dui ex.</p></div></div>
  <div class="toc-item" style="left:285px;top:156px"><span class="toc-num">4</span><div><p class="h-teal">Title Goes Here!</p><p class="txt">Lorem ipsum dolor sit amet, consectetur adipiscing elit. Vivamus eu dui ex.</p></div></div>
  <div class="toc-item" style="left:72px;top:209px"><span class="toc-num">5</span><div><p class="h-teal">Title Goes Here!</p><p class="txt">Lorem ipsum dolor sit amet, consectetur adipiscing elit. Vivamus eu dui ex.</p></div></div>
  <div class="toc-item" style="left:285px;top:209px"><span class="toc-num">6</span><div><p class="h-teal">Title Goes Here!</p><p class="txt">Lorem ipsum dolor sit amet, consectetur adipiscing elit. Vivamus eu dui ex.</p></div></div>
  <p class="foot-name">Plorvane</p><div class="foot-bar">Copyright 2021 Plorvane. All rights reserved &nbsp;|&nbsp; 5</div>
</section>
<section class="slide about" style="left:609px;top:1382px">
  <p class="mark" style="left:40px;right:auto;top:62px">PLORVANE</p>
  <h2 class="abs" style="left:40px;top:84px;font-size:20px;font-weight:400">About <b>Us</b></h2>
  <p class="txt abs" style="left:40px;top:112px;width:200px;font-size:7px">Lorem ipsum dolor sit amet, consectetur adipiscing elit. Vivamus eu dui ex. Curabitur dapibus dignissim dui, in molestie metus feugiat sed. Praesent aliquet lorem ex, eu dapibus odio varius at. Duis eget tellus porta, consequat lacus vitae, venenatis dolor. Nulla facilisi. In et sollicitudin lacus. Donec risus orci, gravida sit amet risus vehicula, aliquet pretium sapien. Nullam sit amet magna non ex bibendum mollis. Nunc vel neque eu augue dignissim congue.</p>
  <div class="frame-block" style="left:248px;top:56px;width:236px;height:8px"></div>
  <div class="frame" style="left:262px;top:70px;width:248px;height:158px"></div>
  <div class="photo" role="img" aria-label="Colleagues reviewing charts at a desk with laptops" style="left:254px;top:62px;width:244px;height:156px;background:linear-gradient(135deg,#e7e3dc,#b9b3a8 60%,#8a8c8a)"></div>
  <p class="foot-name">Plorvane</p><div class="foot-bar">Copyright 2021 Plorvane. All rights reserved &nbsp;|&nbsp; 6</div>
</section>

<!-- row 4: two photos, team -->
<section class="slide" style="left:51px;top:1704px">
  <div class="frame-block" style="left:36px;top:34px;width:204px;height:6px"></div>
  <div class="frame" style="left:46px;top:44px;width:208px;height:104px"></div>
  <div class="photo" role="img" aria-label="Hands stacked together over a table" style="left:40px;top:38px;width:208px;height:100px;background:linear-gradient(135deg,#d9c9b3,#8f7763 60%,#5a4a40)"></div>
  <div class="frame-block" style="left:282px;top:34px;width:204px;height:6px"></div>
  <div class="frame" style="left:292px;top:44px;width:208px;height:104px"></div>
  <div class="photo" role="img" aria-label="Top view of a team working at a wooden table with laptops" style="left:286px;top:38px;width:208px;height:100px;background:linear-gradient(135deg,#a58665,#6f5a48 55%,#3d4c57)"></div>
  <p class="mark" style="left:40px;right:auto;top:154px">PLORVANE</p>
  <h3 class="abs" style="left:40px;top:166px;font-size:14px">Title Goes Here!</h3>
  <p class="txt abs" style="left:40px;top:186px;width:210px;font-size:7px">Lorem ipsum dolor sit amet, consectetur adipiscing elit. Vivamus eu dui ex. Curabitur dapibus dignissim dui, in molestie metus feugiat sed. Praesent aliquet lorem ex, eu dapibus odio varius at.</p>
  <p class="mark" style="left:286px;right:auto;top:154px">PLORVANE</p>
  <h3 class="abs" style="left:286px;top:166px;font-size:14px">Title Goes Here!</h3>
  <p class="txt abs" style="left:286px;top:186px;width:210px;font-size:7px">Lorem ipsum dolor sit amet, consectetur adipiscing elit. Vivamus eu dui ex. Curabitur dapibus dignissim dui, in molestie metus feugiat sed. Praesent aliquet lorem ex, eu dapibus odio varius at.</p>
  <p class="foot-name">Plorvane</p><div class="foot-bar">Copyright 2021 Plorvane. All rights reserved &nbsp;|&nbsp; 7</div>
</section>
<section class="slide" style="left:609px;top:1704px">
  <div class="band" role="img" aria-label="Office team meeting, teal tint" style="height:126px"></div>
  <p class="mark" style="top:18px;color:#fff">PLORVANE</p>
  <h2 class="band-title" style="top:42px;font-size:18px">Meet <b>The Team</b></h2>
  <div class="avatar" role="img" aria-label="Team member portrait" style="left:84px;top:88px"></div>
  <div class="avatar" role="img" aria-label="Team member portrait" style="left:234px;top:88px"></div>
  <div class="avatar" role="img" aria-label="Team member portrait" style="left:384px;top:88px"></div>
  <div class="col" style="left:65px;top:174px"><p class="h-bold">Person Name</p><p class="txt" style="margin-top:1px;color:var(--ink)">Job Title Goes Here!</p><p class="txt">Lorem ipsum dolor sit amet, consectetur adipiscing elit. Vivamus eu dui ex. Curabitur dapibus dignissim dui, in molestie metus feugiat sed.</p></div>
  <div class="col" style="left:215px;top:174px"><p class="h-bold">Person Name</p><p class="txt" style="margin-top:1px;color:var(--ink)">Job Title Goes Here!</p><p class="txt">Lorem ipsum dolor sit amet, consectetur adipiscing elit. Vivamus eu dui ex. Curabitur dapibus dignissim dui, in molestie metus feugiat sed.</p></div>
  <div class="col" style="left:365px;top:174px"><p class="h-bold">Person Name</p><p class="txt" style="margin-top:1px;color:var(--ink)">Job Title Goes Here!</p><p class="txt">Lorem ipsum dolor sit amet, consectetur adipiscing elit. Vivamus eu dui ex. Curabitur dapibus dignissim dui, in molestie metus feugiat sed.</p></div>
  <p class="foot-name">Plorvane</p><div class="foot-bar">Copyright 2021 Plorvane. All rights reserved &nbsp;|&nbsp; 8</div>
</section>

<!-- row 5 -->
<section class="slide" style="left:51px;top:2025px">
  <div class="band" role="img" aria-label="Business meeting over documents, teal tint"></div>
  <p class="mark" style="top:20px;color:#fff">PLORVANE</p>
  <h2 class="band-title"><b>Slide Title</b> Goes Here</h2>
  <p class="band-text">Lorem ipsum dolor sit amet, consectetur adipiscing elit. Vivamus eu dui ex. Curabitur dapibus dignissim dui, in molestie metus feugiat sed. Praesent aliquet lorem ex, eu dapibus odio varius at.</p>
  <svg class="abs" style="left:0;top:144px" width="540" height="12"><g fill="#fff" stroke="var(--teal)" stroke-width="1"><rect x="80" y="2" width="8" height="8"/><rect x="204" y="2" width="8" height="8"/><rect x="327" y="2" width="8" height="8"/><rect x="450" y="2" width="8" height="8"/></g></svg>
  <div class="col" style="left:29px;top:164px"><p class="h-bold" style="border-bottom:1px solid #cfd8da;padding-bottom:3px">Title Goes Here</p><p class="txt">Lorem ipsum dolor sit amet, consectetur adipiscing elit. Vivamus eu dui ex. Curabitur dapibus dignissim dui, in molestie metus feugiat sed. Praesent aliquet lorem ex, eu dapibus odio varius at.</p></div>
  <div class="col" style="left:153px;top:164px"><p class="h-bold" style="border-bottom:1px solid #cfd8da;padding-bottom:3px">Title Goes Here</p><p class="txt">Lorem ipsum dolor sit amet, consectetur adipiscing elit. Vivamus eu dui ex. Curabitur dapibus dignissim dui, in molestie metus feugiat sed. Praesent aliquet lorem ex, eu dapibus odio varius at.</p></div>
  <div class="col" style="left:276px;top:164px"><p class="h-bold" style="border-bottom:1px solid #cfd8da;padding-bottom:3px">Title Goes Here</p><p class="txt">Lorem ipsum dolor sit amet, consectetur adipiscing elit. Vivamus eu dui ex. Curabitur dapibus dignissim dui, in molestie metus feugiat sed. Praesent aliquet lorem ex, eu dapibus odio varius at.</p></div>
  <div class="col" style="left:399px;top:164px"><p class="h-bold" style="border-bottom:1px solid #cfd8da;padding-bottom:3px">Title Goes Here</p><p class="txt">Lorem ipsum dolor sit amet, consectetur adipiscing elit. Vivamus eu dui ex. Curabitur dapibus dignissim dui, in molestie metus feugiat sed. Praesent aliquet lorem ex, eu dapibus odio varius at.</p></div>
  <p class="foot-name">Plorvane</p><div class="foot-bar">Copyright 2021 Plorvane. All rights reserved &nbsp;|&nbsp; 9</div>
</section>
<section class="slide" style="left:609px;top:2025px">
  <p class="mark" style="top:22px">PLORVANE</p>
  <h2 class="title" style="top:44px"><b>Slide Title</b> Goes Here!</h2>
  <div class="ico t abs" style="left:60px;top:100px"><svg viewBox="0 0 10 10"><circle cx="5" cy="5" r="3" fill="#fff"/></svg></div>
  <div class="item" style="left:60px;top:97px"><p class="h-teal">Title Goes Here!</p><p class="txt">Lorem ipsum dolor sit amet, consectetur adipiscing elit. Vivamus eu dui ex. Curabitur dapibus.</p></div>
  <div class="ico d abs" style="left:60px;top:141px"><svg viewBox="0 0 10 10"><rect x="1.5" y="2.5" width="7" height="5" fill="none" stroke="#fff"/></svg></div>
  <div class="item" style="left:60px;top:138px"><p class="h-teal">Title Goes Here!</p><p class="txt">Lorem ipsum dolor sit amet, consectetur adipiscing elit. Vivamus eu dui ex. Curabitur dapibus.</p></div>
  <div class="ico b abs" style="left:60px;top:182px"><svg viewBox="0 0 10 10"><path d="M5 5V1.5A3.5 3.5 0 1 1 1.5 5Z" fill="#fff"/></svg></div>
  <div class="item" style="left:60px;top:179px"><p class="h-teal">Title Goes Here!</p><p class="txt">Lorem ipsum dolor sit amet, consectetur adipiscing elit. Vivamus eu dui ex. Curabitur dapibus.</p></div>
  <div class="ico l abs" style="left:60px;top:223px"><svg viewBox="0 0 10 10"><path d="M2 5.5l2 2 4-5" fill="none" stroke="#fff" stroke-width="1.5"/></svg></div>
  <div class="item" style="left:60px;top:220px"><p class="h-teal">Title Goes Here!</p><p class="txt">Lorem ipsum dolor sit amet, consectetur adipiscing elit. Vivamus eu dui ex. Curabitur dapibus.</p></div>
  <div class="ico b abs" style="left:275px;top:100px"><svg viewBox="0 0 10 10"><rect x="2" y="2" width="6" height="6" fill="none" stroke="#fff"/><path d="M2 4h6" stroke="#fff"/></svg></div>
  <div class="item" style="left:275px;top:97px"><p class="h-teal">Title Goes Here!</p><p class="txt">Lorem ipsum dolor sit amet, consectetur adipiscing elit. Vivamus eu dui ex. Curabitur dapibus.</p></div>
  <div class="ico l abs" style="left:275px;top:141px"><svg viewBox="0 0 10 10"><circle cx="5" cy="5" r="2.5" fill="none" stroke="#fff" stroke-width="1.5"/></svg></div>
  <div class="item" style="left:275px;top:138px"><p class="h-teal">Title Goes Here!</p><p class="txt">Lorem ipsum dolor sit amet, consectetur adipiscing elit. Vivamus eu dui ex. Curabitur dapibus.</p></div>
  <div class="ico d abs" style="left:275px;top:182px"><svg viewBox="0 0 10 10"><path d="M2 8l6-6M5 2h3v3" fill="none" stroke="#fff" stroke-width="1.3"/></svg></div>
  <div class="item" style="left:275px;top:179px"><p class="h-teal">Title Goes Here!</p><p class="txt">Lorem ipsum dolor sit amet, consectetur adipiscing elit. Vivamus eu dui ex. Curabitur dapibus.</p></div>
  <div class="ico b abs" style="left:275px;top:223px"><svg viewBox="0 0 10 10"><path d="M3 2h4v2a2 2 0 0 1-4 0ZM5 6v2M3.5 8.5h3" fill="none" stroke="#fff"/></svg></div>
  <div class="item" style="left:275px;top:220px"><p class="h-teal">Title Goes Here!</p><p class="txt">Lorem ipsum dolor sit amet, consectetur adipiscing elit. Vivamus eu dui ex. Curabitur dapibus.</p></div>
  <p class="foot-name">Plorvane</p><div class="foot-bar">Copyright 2021 Plorvane. All rights reserved &nbsp;|&nbsp; 10</div>
</section>

<!-- row 6 -->
<section class="slide on-dark" style="left:51px;top:2347px;background:linear-gradient(120deg,#23292c 0%,#2f3d42 40%,#3c6a70 75%,#5a9a98 100%)" role="img" aria-label="Colleagues at a laptop, dark teal tint">
  <p class="mark" style="left:46px;right:auto;top:150px;color:#fff;font-size:9px">PLORVANE</p>
  <h2 class="abs" style="left:46px;top:170px;font-size:25px;color:#fff">Section Break</h2>
  <p class="abs" style="left:46px;top:208px;width:260px;font-size:9px;line-height:1.25;color:#e8f1f1">Lorem ipsum dolor sit amet, consectetur adipiscing elit. Vivamus eu dui ex. Curabitur dapibus dignissim dui, in molestie metus.</p>
</section>
<section class="slide" style="left:609px;top:2347px">
  <p class="mark" style="top:20px">PLORVANE</p>
  <h2 class="title" style="top:42px"><b>Slide Title</b> Goes Here!</h2>
  <div class="abs" style="left:40px;top:132px;width:100px;text-align:right"><p class="h-teal">Title Goes Here!</p><p class="txt" style="font-size:6px">Lorem ipsum dolor sit amet, consectetur adipiscing elit. Vivamus eu dui ex. Curabitur dapibus dignissim dui, in molestie metus feugiat sed.</p></div>
  <svg class="abs" style="left:0;top:0" width="540" height="303">
    <line x1="146" y1="130" x2="146" y2="190" stroke="var(--blue)" stroke-width="1.5"/>
    <circle cx="172" cy="160" r="10" fill="var(--blue)"/><circle cx="172" cy="160" r="3.5" fill="none" stroke="#fff" stroke-width="1.5"/>
    <polygon points="270,88 246,130.6 270,136.6" fill="#a4d9cf"/><polygon points="270,88 294,130.6 270,136.6" fill="#7cc3b8"/>
    <polygon points="241.2,139.1 270,146.3 270,191.7 218.8,178.9" fill="#2a9ac0"/><polygon points="298.8,139.1 270,146.3 270,191.7 321.2,178.9" fill="#1f6f90"/>
    <polygon points="214,187.4 270,201.4 270,250 190,230" fill="#3aa396"/><polygon points="326,187.4 270,201.4 270,250 350,230" fill="#2a7f76"/>
    <line x1="355" y1="98" x2="355" y2="150" stroke="var(--teal)" stroke-width="1.5"/>
    <circle cx="378" cy="116" r="10" fill="var(--teal)"/><circle cx="378" cy="114" r="3.5" fill="#fff"/>
    <line x1="355" y1="198" x2="355" y2="252" stroke="var(--navy)" stroke-width="1.5"/>
    <circle cx="378" cy="218" r="10" fill="var(--navy)"/><path d="M374 218l3 3 5-6" stroke="#fff" fill="none" stroke-width="1.5"/>
  </svg>
  <div class="abs" style="left:396px;top:94px;width:110px"><p class="h-teal">Title Goes Here!</p><p class="txt" style="font-size:6px">Lorem ipsum dolor sit amet, consectetur adipiscing elit. Vivamus eu dui ex. Curabitur dapibus dignissim dui, in molestie metus feugiat sed.</p></div>
  <div class="abs" style="left:396px;top:198px;width:110px"><p class="h-teal">Title Goes Here!</p><p class="txt" style="font-size:6px">Lorem ipsum dolor sit amet, consectetur adipiscing elit. Vivamus eu dui ex. Curabitur dapibus dignissim dui, in molestie metus feugiat sed.</p></div>
  <div class="foot-bar" style="left:62px">Copyright 2021 Plorvane. All rights reserved &nbsp;|&nbsp; 12</div><p class="foot-name">Plorvane</p>
</section>

<!-- row 7 -->
<section class="slide" style="left:51px;top:2669px">
  <p class="mark" style="top:20px">PLORVANE</p>
  <h2 class="title" style="top:42px;font-weight:400">Our Process</h2>
  <svg class="abs" style="left:0;top:112px" width="540" height="30"><line x1="0" y1="15" x2="530" y2="15" stroke="#9fb2b5" stroke-width="1" stroke-dasharray="2 2"/><path d="M526 11l6 4-6 4" fill="none" stroke="#9fb2b5"/></svg>
  <div class="step t" style="left:92px;top:112px">1</div>
  <div class="step b" style="left:200px;top:112px">2</div>
  <div class="step t" style="left:308px;top:112px">3</div>
  <div class="step b" style="left:416px;top:112px">4</div>
  <div class="col" style="left:52px;top:160px"><p class="h-teal" style="font-size:9px;line-height:1.1">Title Goes<br>Here!</p><p class="txt" style="font-size:6px">Lorem ipsum dolor sit amet, consectetur adipiscing elit. Vivamus eu dui ex. Curabitur dapibus dignissim dui, in molestie metus.</p></div>
  <div class="col" style="left:160px;top:160px"><p class="h-teal" style="font-size:9px;line-height:1.1;color:var(--blue)">Title Goes<br>Here!</p><p class="txt" style="font-size:6px">Lorem ipsum dolor sit amet, consectetur adipiscing elit. Vivamus eu dui ex. Curabitur dapibus dignissim dui, in molestie metus.</p></div>
  <div class="col" style="left:268px;top:160px"><p class="h-teal" style="font-size:9px;line-height:1.1">Title Goes<br>Here!</p><p class="txt" style="font-size:6px">Lorem ipsum dolor sit amet, consectetur adipiscing elit. Vivamus eu dui ex. Curabitur dapibus dignissim dui, in molestie metus.</p></div>
  <div class="col" style="left:376px;top:160px"><p class="h-teal" style="font-size:9px;line-height:1.1;color:var(--blue)">Title Goes<br>Here!</p><p class="txt" style="font-size:6px">Lorem ipsum dolor sit amet, consectetur adipiscing elit. Vivamus eu dui ex. Curabitur dapibus dignissim dui, in molestie metus.</p></div>
  <p class="foot-name">Plorvane</p><div class="foot-bar">Copyright 2021 Plorvane. All rights reserved &nbsp;|&nbsp; 13</div>
</section>
<section class="slide" style="left:609px;top:2669px">
  <div class="band" role="img" aria-label="City aerial view, teal tint" style="background:linear-gradient(110deg,#2c8f92 0%,#2b7e93 50%,#236a86 100%)"></div>
  <p class="mark" style="top:20px;color:#fff">PLORVANE</p>
  <h2 class="band-title"><b>Slide Title</b> Goes Here</h2>
  <p class="band-text">Lorem ipsum dolor sit amet, consectetur adipiscing elit. Vivamus eu dui ex. Curabitur dapibus dignissim dui, in molestie metus feugiat sed. Praesent aliquet lorem ex, eu dapibus odio varius at.</p>
  <svg class="abs" style="left:0;top:134px" width="540" height="34"><g stroke="#fff" stroke-width="2.5"><circle cx="84" cy="17" r="14" fill="var(--teal)"/><circle cx="208" cy="17" r="14" fill="var(--blue)"/><circle cx="331" cy="17" r="14" fill="var(--teal)"/><circle cx="454" cy="17" r="14" fill="var(--blue)"/></g>
  <g fill="none" stroke="#fff" stroke-width="1.3"><circle cx="84" cy="15" r="4"/><path d="M82 21h4"/><circle cx="208" cy="17" r="5"/><circle cx="208" cy="17" r="2"/><path d="M326 22v-4M330 22v-7M334 22v-5"/><path d="M450 11h8v3a4 4 0 0 1-8 0Z M454 18v3M451 22h6"/></g></svg>
  <div class="col" style="left:29px;top:172px"><p class="h-bold" style="font-weight:400">Title Goes Here</p><p class="txt">Lorem ipsum dolor sit amet, consectetur adipiscing elit. Vivamus eu dui ex. Curabitur dapibus dignissim dui, in molestie metus feugiat sed.</p></div>
  <div class="col" style="left:153px;top:172px"><p class="h-bold" style="color:var(--blue)">Title Goes Here</p><p class="txt">Lorem ipsum dolor sit amet, consectetur adipiscing elit. Vivamus eu dui ex. Curabitur dapibus dignissim dui, in molestie metus feugiat sed.</p></div>
  <div class="col" style="left:276px;top:172px"><p class="h-bold" style="font-weight:400">Title Goes Here</p><p class="txt">Lorem ipsum dolor sit amet, consectetur adipiscing elit. Vivamus eu dui ex. Curabitur dapibus dignissim dui, in molestie metus feugiat sed.</p></div>
  <div class="col" style="left:399px;top:172px"><p class="h-bold" style="color:var(--blue)">Title Goes Here</p><p class="txt">Lorem ipsum dolor sit amet, consectetur adipiscing elit. Vivamus eu dui ex. Curabitur dapibus dignissim dui, in molestie metus feugiat sed.</p></div>
  <p class="foot-name">Plorvane</p><div class="foot-bar">Copyright 2021 Plorvane. All rights reserved &nbsp;|&nbsp; 14</div>
</section>

<!-- row 8 -->
<section class="slide" style="left:51px;top:2990px">
  <p class="mark" style="top:20px">PLORVANE</p>
  <h2 class="title" style="top:42px;font-weight:400">Chart <b>Slide</b></h2>
  <svg class="abs" style="left:30px;top:92px" width="240" height="160" font-family="Arimo, sans-serif" font-size="4.5" fill="#6b7479">
    <g stroke="#e4e9ea" stroke-width=".6"><line x1="20" y1="10" x2="225" y2="10"/><line x1="20" y1="32" x2="225" y2="32"/><line x1="20" y1="54" x2="225" y2="54"/><line x1="20" y1="76" x2="225" y2="76"/><line x1="20" y1="98" x2="225" y2="98"/><line x1="20" y1="120" x2="225" y2="120"/><line x1="20" y1="142" x2="225" y2="142" stroke="#9aa6a9"/></g>
    <g text-anchor="end"><text x="14" y="12">6</text><text x="14" y="34">5</text><text x="14" y="56">4</text><text x="14" y="78">3</text><text x="14" y="100">2</text><text x="14" y="122">1</text><text x="14" y="144">0</text></g>
    <g>
      <rect x="28" y="47.4" width="7" height="94.6" fill="#1f7fa8"/><rect x="37" y="89.2" width="7" height="52.8" fill="#2f9e94"/><rect x="46" y="98" width="7" height="44" fill="#13232a"/>
      <rect x="62" y="87" width="7" height="55" fill="#1f7fa8"/><rect x="71" y="45.2" width="7" height="96.8" fill="#2f9e94"/><rect x="80" y="98" width="7" height="44" fill="#13232a"/>
      <rect x="96" y="65" width="7" height="77" fill="#1f7fa8"/><rect x="105" y="102.4" width="7" height="39.6" fill="#2f9e94"/><rect x="114" y="76" width="7" height="66" fill="#13232a"/>
      <rect x="130" y="43" width="7" height="99" fill="#1f7fa8"/><rect x="139" y="80.4" width="7" height="61.6" fill="#2f9e94"/><rect x="148" y="32" width="7" height="110" fill="#13232a"/>
      <rect x="164" y="47.4" width="7" height="94.6" fill="#1f7fa8"/><rect x="173" y="89.2" width="7" height="52.8" fill="#2f9e94"/><rect x="182" y="98" width="7" height="44" fill="#13232a"/>
      <rect x="198" y="87" width="7" height="55" fill="#1f7fa8"/><rect x="207" y="45.2" width="7" height="96.8" fill="#2f9e94"/><rect x="216" y="98" width="7" height="44" fill="#13232a"/>
    </g>
    <g text-anchor="middle"><text x="40" y="151">Category 1</text><text x="74" y="151">Category 2</text><text x="108" y="151">Category 3</text><text x="142" y="151">Category 4</text><text x="176" y="151">Category 5</text><text x="210" y="151">Category 6</text></g>
  </svg>
  <p class="txt abs" style="left:278px;top:94px;width:230px;font-size:5.5px">Lorem ipsum dolor sit amet, at laborum nibh duis mauris. Per ultrices lectus sed metus tristique eu. Diam suspendisse ac ipsum maecenas fermentum, aliquet imperdiet et lobortis venenatis nascetur lacus. A ac, vivamus erat nullam.</p>
  <div class="abs" style="left:278px;top:138px;width:230px">
    <table class="mini"><tr><th>Category</th><th class="s">Series 1</th><th class="s" style="background:var(--blue)">Series 2</th><th class="s">Series 3</th></tr>
    <tr><td>Category 1</td><td class="n">4.3</td><td class="n">2.4</td><td class="n">2</td></tr>
    <tr><td>Category 2</td><td class="n">2.5</td><td class="n">4.4</td><td class="n">2</td></tr>
    <tr><td>Category 3</td><td class="n">3.5</td><td class="n">1.8</td><td class="n">3</td></tr>
    <tr><td>Category 4</td><td class="n">4.5</td><td class="n">2.8</td><td class="n">5</td></tr>
    <tr><td>Category 5</td><td class="n">4.3</td><td class="n">2.4</td><td class="n">2</td></tr>
    <tr><td>Category 6</td><td class="n">2.5</td><td class="n">4.4</td><td class="n">2</td></tr></table>
  </div>
  <p class="foot-name">Plorvane</p><div class="foot-bar">Copyright 2021 Plorvane. All rights reserved &nbsp;|&nbsp; 15</div>
</section>
<section class="slide" style="left:609px;top:2990px">
  <p class="mark" style="top:20px">PLORVANE</p>
  <h2 class="title" style="top:42px;font-weight:400">Table <b>Slide</b></h2>
  <div class="abs" style="left:25px;top:88px;width:490px">
    <table class="big"><tr><th style="width:130px">Heading</th><th>Title 1</th><th>Title 2</th><th>Title 3</th><th>Title 4</th><th>Title 5</th></tr>
    <tr><td>Lorem ipsum dolor sit amet</td><td>12</td><td>12</td><td>43</td><td>87</td><td>34</td></tr>
    <tr><td>Lorem ipsum dolor sit amet</td><td>45</td><td>34</td><td>34</td><td>12</td><td>55</td></tr>
    <tr><td>Lorem ipsum dolor sit amet</td><td>66</td><td>56</td><td>67</td><td>34</td><td>67</td></tr>
    <tr><td>Lorem ipsum dolor sit amet</td><td>78</td><td>90</td><td>23</td><td>56</td><td>12</td></tr>
    <tr><td>Lorem ipsum dolor sit amet</td><td>65</td><td>98</td><td>45</td><td>77</td><td>34</td></tr>
    <tr><td>Lorem ipsum dolor sit amet</td><td>23</td><td>67</td><td>55</td><td>87</td><td>11</td></tr>
    <tr><td>Lorem ipsum dolor sit amet</td><td>44</td><td>55</td><td>67</td><td>66</td><td>89</td></tr></table>
  </div>
  <p class="foot-name">Plorvane</p><div class="foot-bar">Copyright 2021 Plorvane. All rights reserved &nbsp;|&nbsp; 16</div>
</section>

<!-- contact -->
<section class="slide contact" style="left:331px;top:3312px" role="img" aria-label="Aerial view of city towers, dark teal tint">
  <p class="abs" style="left:55px;top:128px;font-size:18px;font-weight:700;color:#fff">Plorvane</p>
  <p class="abs" style="left:55px;top:146px;font-size:9px;font-weight:700;color:#fff">Contact Us</p>
  <ul class="contact-list" style="top:168px">
    <li><svg viewBox="0 0 10 10"><path d="M2 1h2l1 2.5-1.3 1a5 5 0 0 0 2.3 2.3l1-1.3L9.5 6.5v2a1 1 0 0 1-1 1A8 8 0 0 1 1 2a1 1 0 0 1 1-1Z" fill="#fff"/></svg>555-0142-7781</li>
    <li><svg viewBox="0 0 10 10"><circle cx="5" cy="5" r="4" fill="none" stroke="#fff"/><circle cx="5" cy="5" r="1.6" fill="none" stroke="#fff"/></svg>info@crewplorvane.com</li>
    <li><svg viewBox="0 0 10 10"><circle cx="5" cy="5" r="4" fill="none" stroke="#fff"/><path d="M1 5h8M5 1c-2 2.5-2 5.5 0 8M5 1c2 2.5 2 5.5 0 8" fill="none" stroke="#fff" stroke-width=".7"/></svg>www.crewplorvane.com</li>
  </ul>
  <p class="abs" style="left:0;right:0;bottom:6px;text-align:center;font-size:4.5px;color:#d7e6e6">Copyright 2021 Plorvane. All rights reserved</p>
</section>

</main>
</body>
</html>
```